For Sale Sign for Real Estate Agency

We need a For Sale Sign designed for our agency. I want a very simple/elegant sign that says "For Sale" towards the top of the sign (not in huge letters). Most of the sign should be a design/picture with our name and phone number somewhere at the bottom.

One significant detail, it's important that our logo not be too big or the center piece of the sign. Since our company name has the word "rent" in it, people assume the house is for rent, instead of for sale.

I attached our logo and a rough outline of the format I'm looking for.

Again, I'm looking for elegant and simple! Thanks for your time

Industry/Entity Type

Real Estate

Colors

Designer to choose colors to be used in the design.

Requirements
Must have
Nice to have
Should not have
• Nothing tacky!
• Our logo/company name should not be too big or the center piece of the sign. Since our company name has the word "rent" in it, people assume the house is for rent, instead of for sale.

```html
<!DOCTYPE html>
<html lang="en">
<head>
<meta charset="utf-8">
<title>HomeVale Realty – For Sale Sign</title>
<link rel="stylesheet" href="https://fonts.googleapis.com/css2?family=Montserrat:wght@500;800&display=swap">
<style>
  :root {
    --bg: #ffffff;
    --sign-white: #ffffff;
    --brand-red: #e63024;
    --brand-red-soft: #ea4a3f;
    --ink: #161616;
    --text-light: #ffffff;
  }
  html, body {
    margin: 0;
    padding: 0;
    width: 1087px;
    height: 1200px;
    overflow: hidden;
    background: var(--bg);
  }
  .canvas {
    position: relative;
    width: 1087px;
    height: 1200px;
  }
  .sign {
    position: absolute;
    left: 307px;
    top: 284px;
    width: 476px;
    height: 634px;
    background: var(--sign-white);
    overflow: hidden;
    outline: 1px solid #eeeeee;
  }
  .sign-art {
    position: absolute;
    inset: 0;
    width: 476px;
    height: 634px;
  }
  .hero-art {
    position: absolute;
    left: 93px;
    top: 70px;
    width: 294px;
    height: 255px;
    background: linear-gradient(180deg, var(--brand-red-soft), var(--brand-red));
  }
  .agency-name {
    position: absolute;
    left: 35px;
    top: 23px;
    font-family: "Montserrat", sans-serif;
    font-weight: 500;
    color: var(--ink);
    line-height: 1;
  }
  .agency-name .name {
    display: block;
    font-size: 27px;
    letter-spacing: -0.5px;
  }
  .agency-name .suffix {
    display: block;
    text-align: right;
    font-size: 15px;
    letter-spacing: 1.5px;
    margin-top: 3px;
  }
  .headline {
    position: absolute;
    left: 0;
    right: 0;
    top: 346px;
    margin: 0;
    text-align: center;
    font-family: "Montserrat", sans-serif;
    font-weight: 800;
    font-size: 68px;
    line-height: 1;
    color: var(--ink);
  }
  .phone {
    position: absolute;
    left: 0;
    right: 0;
    top: 533px;
    margin: 0;
    text-align: center;
    font-family: "Montserrat", sans-serif;
    font-weight: 800;
    font-size: 58px;
    line-height: 1;
    color: var(--text-light);
  }
</style>
</head>
<body>
<div class="canvas">
  <div class="sign">
    <svg class="sign-art" viewBox="0 0 476 634" aria-hidden="true">
      <path class="accent-wave" fill="var(--brand-red)" d="M0,498 Q238,382 476,498 L476,634 L0,634 Z"/>
      <path class="footer-wave" fill="var(--ink)" d="M0,516 Q238,418 476,516 L476,634 L0,634 Z"/>
    </svg>
    <div class="hero-art" role="img" aria-label="Red house illustration with a chimney"></div>
    <div class="agency-name">
      <span class="name">HomeVale</span>
      <span class="suffix">Realty</span>
    </div>
    <h1 class="headline">FOR SALE</h1>
    <p class="phone">401-555-0148</p>
  </div>
</div>
</body>
</html>
```